Quorvane - corporate Business Card

We need a good look and innovative business card for a new start up company based in Los Angeles called "Quorvane". We are in a payment business, including payment card, app, and ewallet. We are expert in online payment and Card not present (CNP) transaction.
We need an innovative, modern business card.

Our logo font is Aero Matics

Target Market(s)

Startup - Bank - Online Payment - Card Manufacturing

Industry/Entity Type

Startup

Contact Information for Business Card

phone: 424 555 0173 - Address: 4270 Marbrook blvd, Dunmere Heights, CA 90417

Requirements
Must have
• Message: innovative, professional, expert, high tech, trust, online payment expert, security
Nice to have
• no comment
Should not have
• no Comment

```html
<!DOCTYPE html>
<html lang="en">
<head>
<meta charset="utf-8">
<title>Quorvane – Business Card</title>
<link rel="stylesheet" href="https://fonts.googleapis.com/css2?family=Exo+2:wght@500;600;700&display=swap">
<style>
  :root {
    --backdrop: #1f1f21;
    --card-white: #f4f4f4;
    --card-white-edge: #e2e2e2;
    --brand-red: #b91f2e;
    --ink-white: #ffffff;
    --divider: rgba(255, 255, 255, 0.45);
  }
  * { box-sizing: border-box; margin: 0; padding: 0; }
  html, body {
    width: 1200px;
    height: 852px;
    overflow: hidden;
    background: var(--backdrop);
    font-family: "Exo 2", "Segoe UI", sans-serif;
  }
  .canvas {
    position: relative;
    width: 1200px;
    height: 852px;
  }
  .card {
    position: absolute;
    top: 271px;
    width: 525px;
    height: 310px;
    border-radius: 22px;
    box-shadow: 0 14px 30px rgba(0, 0, 0, 0.5);
  }
  .card--front {
    left: 50px;
    background: radial-gradient(ellipse at 55% 50%, #ffffff 0%, var(--card-white) 55%, var(--card-white-edge) 100%);
    display: flex;
    align-items: center;
    justify-content: center;
    gap: 14px;
  }
  .brand-dot {
    width: 60px;
    height: 60px;
    border-radius: 50%;
    background: var(--brand-red);
  }
  .brand-name {
    font-weight: 700;
    font-size: 54px;
    letter-spacing: 1px;
    color: var(--brand-red);
    line-height: 1;
  }
  .card--back {
    left: 625px;
    background: var(--brand-red);
  }
  .back-mark {
    position: absolute;
    left: 52px;
    top: 112px;
    width: 124px;
    height: 124px;
    border-radius: 50%;
    background: var(--ink-white);
  }
  .back-divider {
    position: absolute;
    left: 222px;
    top: 70px;
    width: 1px;
    height: 150px;
    background: linear-gradient(to bottom, transparent, var(--divider), transparent);
  }
  .contact {
    position: absolute;
    left: 246px;
    top: 92px;
    color: var(--ink-white);
    font-weight: 500;
    font-size: 14.5px;
    line-height: 1.45;
    white-space: nowrap;
  }
  .contact__address { margin-bottom: 4px; }
  .contact__row {
    display: flex;
    align-items: center;
    gap: 7px;
  }
  .contact__icon {
    width: 14px;
    height: 14px;
    flex: none;
  }
</style>
</head>
<body>
<main class="canvas">
  <section class="card card--front" aria-label="Business card front">
    <span class="brand-dot"></span>
    <span class="brand-name">quorvane</span>
  </section>

  <section class="card card--back" aria-label="Business card back">
    <span class="back-mark"></span>
    <span class="back-divider"></span>
    <div class="contact">
      <p class="contact__address">4270 Marbrook blvd<br>Dunmere Heights, CA 90417</p>
      <p class="contact__row">
        <svg class="contact__icon" viewBox="0 0 14 14" aria-hidden="true">
          <circle cx="7" cy="7" r="7" fill="#ffffff"/>
          <path d="M4.4 3.6l1.4-.3.8 1.8-.9.7c.4.9 1.1 1.6 2 2l.7-.9 1.8.8-.3 1.4c-3 .2-5.7-2.5-5.5-5.5z" fill="#b91f2e"/>
        </svg>
        424 555 0173
      </p>
      <p class="contact__row">
        <svg class="contact__icon" viewBox="0 0 14 14" aria-hidden="true">
          <circle cx="7" cy="7" r="7" fill="#ffffff"/>
          <rect x="3.5" y="4.6" width="7" height="4.8" rx="0.6" fill="#b91f2e"/>
          <path d="M3.8 5l3.2 2.4L10.2 5" stroke="#ffffff" stroke-width="0.8" fill="none"/>
        </svg>
        hello@quorvane.example
      </p>
    </div>
  </section>
</main>
</body>
</html>
```